Onlineshop VORMA braucht ein Design!
Zielgruppe
Wir entwickeln innovative Produkte. Für dieses Projekt haben wir 2 Zielgruppen: Kinder und Erwachsene.
Hallo,
wir haben ein neuartiges Tragesystem entwickelt, das dem Träger der Tasche das Tragen erleichtert. Im Moment arbeiten wir daran, dieses System für eine eigene Schultaschenlinie zu verwenden. Später wollen wir unsere Produktpalette erweitern und ebenso Zubehör hierzu(z.B. Regenschirm, Mütze etc.) mit anbieten. Als weiterer Schritt sind zudem auch andere Taschen (z.B. Rucksäcke) für Erwachsene geplant.
Unser Produkt ist einmalig und genau deshalb möchten wir eine Homepage mit Shopware 4 Community Edition eine prägnanten und übersichtlichen Shop, sowie ein Blog erstellen.
Das Logo für unser Schultaschenprojekt befindet sich im Anhang und kann farblich angepasst werden. Wir benötigen einen kindergerechten, gleichzeitig seriösen Internetauftritt und es kann auch gerne ein komplettes Template erstellt werden für Shopware 4 oder ein Design-Vorschlag (Photoshop) eingebracht werden.
Wir bitten euch die Photoshop-Design Vorlagen ohne verbundene Ebenen und Pfade anzulegen. Bei Templates, bitten wir um eine genauere detaillierte Information zum Aufbau, Struktur etc..

```html
<!DOCTYPE html>
<html lang="de">
<head>
<meta charset="utf-8">
<title>VORMA – Rucksäcke</title>
<link href="https://fonts.googleapis.com/css2?family=Arimo:wght@400;700&family=PT+Sans:wght@400;700&display=swap" rel="stylesheet">
<style>
:root{
  --red:#d6112a;--red-dark:#b50a1f;--ink:#4a4a4a;--mute:#8a8a8a;--faint:#b9b9b9;
  --line:#dcdcdc;--panel:#f3f3f3;--bar:#5a5a5a;--white:#fff;
}
*{box-sizing:border-box;margin:0;padding:0}
html,body{width:728px;height:1200px;overflow:hidden;background:var(--white)}
body{position:relative;font-family:Arimo,Arial,sans-serif;color:var(--ink);font-size:8px}
.abs{position:absolute}
.topbar{left:0;top:0;width:728px;height:32px;background:linear-gradient(#4e4e4e,#6a6a6a)}
.topbar .links{left:32px;top:5px;color:#e8e8e8;font-size:7.5px;font-weight:700}
.topbar input{position:absolute;height:12px;border:1px solid #ccc;background:#fff;font-size:6px;color:#aaa;padding-left:3px}
.login{left:534px;top:9px;width:44px;height:12px;background:#888;color:#eee;font-size:6px;text-align:center;line-height:12px}
.forgot{left:591px;top:8px;font-size:5.5px;color:#bbb;font-style:italic;line-height:7px}
.register{left:636px;top:9px;width:60px;height:13px;background:linear-gradient(#c4e23e,#8fbf14);color:#fff;font-size:6.5px;text-align:center;line-height:13px;font-weight:700}
.header{left:0;top:32px;width:728px;height:61px;background:#ececec;border-bottom:1px solid #ddd}
.logo{left:33px;top:40px;font-family:"PT Sans",sans-serif;font-weight:700;font-size:34px;color:var(--red);letter-spacing:1px}
.round{width:29px;height:29px;border-radius:50%;background:radial-gradient(circle at 40% 35%,#fff,#9fc0dd 70%)}
.cart{left:540px;top:38px;width:156px;height:47px;background:#f7f7f7;border:1px solid #e2e2e2;padding:3px 5px;font-size:7px;color:var(--mute)}
.cart b{color:#777;font-size:8.5px;display:block;margin-bottom:2px}
.cart em{color:var(--red);font-style:normal}
.cart u{display:block;margin:6px 0 0 12px}
.nav{left:32px;top:95px;width:663px;height:32px;display:flex;border:1px solid #ddd;font-family:"PT Sans",sans-serif;font-size:12px}
.nav div{display:flex;align-items:center;justify-content:center;color:#888;background:linear-gradient(#fafafa,#e4e4e4);border-right:1px solid #ddd}
.nav .hot{background:linear-gradient(#e6374b,var(--red-dark));color:#fff}
.crumb{left:32px;top:133px;font-size:7px;color:var(--mute)}
.crumb b{color:var(--red);font-weight:400}
.rule{height:1px;background:var(--line)}
.side{left:32px;top:147px;width:136px;height:706px;border:1px solid #e4e4e4}
.cat{left:38px;width:125px;height:50px;border:1px solid #e2e2e2;background:linear-gradient(#fff 30%,#ececec 70%,#fff)}
.cat h3{position:absolute;left:4px;top:5px;font-size:11px;font-weight:400;color:#999}
.cat a{position:absolute;left:5px;top:33px;color:var(--red);font-size:7px}
.cat .pic{position:absolute;right:8px;top:6px;width:30px;height:37px;border-radius:4px}
.box{left:38px;width:125px;border:1px solid #e2e2e2;background:#fff}
.box h3{font-size:11px;font-weight:400;color:#999;padding:4px 4px}
.filter div{position:relative;height:18px;font-size:7px;color:var(--mute);padding:3px 5px}
.filter span{position:absolute;left:45px;top:3px;width:72px;height:12px;border:1px solid #88a;background:#fff;color:#333;padding-left:2px;line-height:11px}
.hero{left:175px;top:147px;width:521px;height:194px;background:linear-gradient(160deg,#fff 10%,#f7d6db 55%,#fbe7ea);border:1px solid #e4e4e4;overflow:hidden}
.hero h1{position:absolute;left:9px;top:11px;font-size:11.5px;color:#555}
.hero ul{position:absolute;left:12px;top:36px;list-style:none;font-size:8.5px;color:#777;line-height:11.5px}
.hero li svg{vertical-align:-2px;margin-right:5px}
.hero .bag{position:absolute;left:230px;top:60px;width:100px;height:134px;border-radius:40px 40px 6px 6px;background:linear-gradient(#3a3e48,#1d2027)}
.buy{left:578px;top:316px;width:122px;height:20px;background:linear-gradient(#e33347,var(--red-dark));color:#fff;font-weight:700;font-size:8.5px;padding:4px 6px;letter-spacing:.3px}
.tagline{left:175px;top:346px;width:360px;font-size:6.5px;line-height:11px}
.offers{left:175px;top:373px;width:521px;height:157px;border:1px solid #e2e2e2;background:#f6f6f6}
.bandhead{height:24px;background:linear-gradient(#fff,#e9e9e9);font-size:8.5px;color:#666;padding:7px 9px}
.prod{position:absolute;top:30px;width:100px;text-align:center;font-size:6.5px;line-height:11px}
.prod .pic{width:50px;height:64px;margin:0 auto 6px;border-radius:14px 14px 4px 4px}
.prod b{display:block;color:var(--red);font-weight:400;font-size:11.5px;margin-top:4px}
.col{top:574px;height:166px;border:1px solid #e6e6e6;background:#fafafa}
.col h4{font-size:8.5px;font-weight:400;color:var(--faint);padding:7px 6px}
.adv{position:relative;padding-left:38px;margin:0 0 10px;font-size:7px;font-weight:700;color:#c9a5aa;line-height:9px}
.adv small{display:block;font-weight:400;color:#aaa;margin-top:2px}
.adv svg{position:absolute;left:10px;top:0}
.h2{left:175px;top:766px;font-size:8.5px;color:#555}
.tab{top:785px;width:62px;height:16px;background:linear-gradient(#fff,#ddd);border:1px solid #ccc;text-align:center;font-size:5.5px;line-height:7px;padding-top:1px}
.para{font-size:7.5px;color:var(--faint);line-height:11.5px}
.foot-h{position:absolute;font-size:7.5px;font-weight:400;color:var(--mute);white-space:nowrap}
.foot-list{position:absolute}
.foot-list li{list-style:none;font-size:7.5px;color:var(--mute);line-height:9.2px}
.foot-list li:before{content:"» ";color:#bbb}
.chips{position:absolute;display:flex;gap:2px}
.chip{height:14px;padding:0 4px;border:1px solid #ddd;background:#f5f5f5;font-size:6px;line-height:13px;color:#555}
</style>
</head>
<body>

<div class="abs topbar">
  <div class="abs links">Datenupload | Versand &amp; Zahlung | Mein Konto | Blog | Kontakt | Impressum</div>
  <input style="left:360px;top:9px;width:83px" value="Benutzername" aria-label="Benutzername">
  <input style="left:450px;top:9px;width:84px" value="Passwort" aria-label="Passwort">
  <div class="abs login">LOGIN</div>
  <div class="abs forgot">Passwort<br>vergessen?</div>
  <div class="abs register">Registrieren</div>
</div>

<div class="abs header"></div>
<div class="abs logo">VORMA</div>
<div class="abs round" style="left:452px;top:46px"></div>
<div class="abs round" style="left:493px;top:46px"></div>
<div class="abs cart"><b>WARENKORB</b>Gesamt: <em>2 Artikel</em> &nbsp;Summe: <em>€ 129,99</em><u>1 Produkt auf dem Merkzettel</u></div>

<nav class="abs nav">
  <div style="width:86px">Home</div>
  <div class="hot" style="width:126px">Produkte &nbsp;⌄</div>
  <div style="width:116px">Druckvorlagen ⌄</div>
  <div style="width:88px">Service &nbsp;⌄</div>
  <div style="width:90px">Über uns</div>
  <div class="hot" style="width:157px">Sonderanfertigung</div>
</nav>

<div class="abs crumb">Startseite &gt;&gt; Produkte &gt;&gt; &nbsp;<b>Rucksäcke</b></div>
<div class="abs rule" style="left:232px;top:137px;width:464px"></div>

<aside class="abs side"></aside>
<div class="abs cat" style="top:153px"><h3>Schultaschen</h3><a>&gt;&gt; Jetzt Shoppen</a><div class="pic" role="img" aria-label="Schulrucksack in Grün und Grau" style="background:linear-gradient(#9cc43a,#444)"></div></div>
<div class="abs rule" style="left:38px;top:212px;width:125px"></div>
<div class="abs cat" style="top:222px"><h3>Freizeit</h3><a>&gt;&gt; Jetzt Shoppen</a><div class="pic" role="img" aria-label="Schwarzer Regenschirm" style="background:linear-gradient(#555,#222)"></div></div>
<div class="abs rule" style="left:38px;top:282px;width:125px"></div>
<div class="abs cat" style="top:292px"><h3>Business</h3><a>&gt;&gt; Jetzt Shoppen</a><div class="pic" role="img" aria-label="Schwarze Aktentasche" style="background:linear-gradient(#444,#111)"></div></div>
<div class="abs rule" style="left:38px;top:351px;width:125px"></div>
<div class="abs box filter" style="top:362px;height:74px"><h3>Produktfilter</h3>
  <div>Hersteller<span>Alle</span></div><div>Produkt<span>Alle</span></div><div>Marke<span>Alle</span></div></div>
<div class="abs rule" style="left:38px;top:446px;width:125px"></div>
<div class="abs box" style="top:455px;height:140px;background:#f4f4f4">
  <div class="abs" style="left:38px;top:4px;width:44px;height:44px;border-radius:50%;background:#c9c9c9" role="img" aria-label="Bewertungssiegel"></div>
  <div class="abs" style="left:26px;top:52px;font-size:11px;letter-spacing:1px;color:#e8b21b">★★★★★</div>
  <div class="abs" style="left:16px;top:64px;width:92px;height:75px;background:#fff;border:1px solid #ddd;text-align:center">
    <div style="font-size:14px;font-family:'PT Sans',sans-serif;color:#222">Exzellent</div>
    <div style="font-size:5.5px;color:#8bb23a">aus 1214 Bewertungen von echten Kunden</div>
    <div style="font-size:5.5px;text-align:left;padding:6px 5px;color:#333">Tolles Produkt, schnelle Lieferung, alles superJjj</div>
    <div style="font-size:5.5px;color:#999;text-align:left;padding:0 3px">17.01.2012 <span style="margin-left:42px">mehr</span></div>
  </div>
</div>
<div class="abs rule" style="left:38px;top:605px;width:125px"></div>
<div class="abs box" style="top:616px;height:73px"><h3 style="font-size:8.5px;line-height:11px">Lorem Ipsum<br>Umfrage</h3>
  <div style="font-size:7px;color:var(--faint);padding:6px 5px;line-height:11px;background:#f4f4f4">○ Lorem ipsum<br>○ Dolor sit amet</div>
  <div style="position:absolute;right:2px;bottom:2px;color:var(--red);font-size:7px">&gt;&gt; Weiter</div></div>
<div class="abs rule" style="left:38px;top:697px;width:125px"></div>
<div class="abs box" style="top:707px;height:140px;background:linear-gradient(#fff 40%,#efefef)">
  <div class="abs" style="left:12px;top:74px;color:var(--red);font-size:8.5px;font-weight:700">Newsletter abonnieren</div>
  <div class="abs para" style="left:18px;top:89px;width:96px;font-size:7px;line-height:11px">Exclusive Angebote und Infos zu unseren Produkten?</div>
  <div class="abs" style="left:18px;top:125px;font-size:7px">&gt;&gt; Jetzt anmelden</div>
</div>
<div class="abs" style="left:26px;top:700px;width:48px;height:48px;border-radius:50%;background:var(--red);color:#fff;font-size:9px;text-align:center;line-height:44px">€2</div>

<section class="abs hero">
  <h1>Seien Sie stolz auf Ihr Logo und Präsentieren Sie es</h1>
  <ul>
    <li><svg width="10" height="9"><path d="M1 5l3 3 5-7" stroke="#d6112a" stroke-width="2" fill="none"/></svg>Top Preise</li>
    <li><svg width="10" height="9"><path d="M1 5l3 3 5-7" stroke="#d6112a" stroke-width="2" fill="none"/></svg>Mindestauflage von nur 10 Stück!</li>
    <li><svg width="10" height="9"><path d="M1 5l3 3 5-7" stroke="#d6112a" stroke-width="2" fill="none"/></svg>Professionell und individuell</li>
  </ul>
  <div class="bag" role="img" aria-label="Schwarzer Rucksack"></div>
</section>
<div class="abs buy">&gt;&gt; JETZT KAUFEN</div>
<p class="abs tagline">Ihr Spezialist für professionelle und individuelle Schultaschen in hochwertiger Qualität, die sich jeder leisten kann.</p>

<section class="abs offers">
  <div class="bandhead">NEUSTE ANGEBOTE</div>
  <div class="prod" style="left:14px"><div class="pic" role="img" aria-label="Rucksack grün-grau" style="background:linear-gradient(#8fb93a,#333)"></div>Lorem Ipsum<br>dolor<b>ab 19,50 EUR</b></div>
  <div class="prod" style="left:133px"><div class="pic" role="img" aria-label="Rucksack olivgrün" style="background:linear-gradient(#6b7a3f,#4a5a30)"></div>Lorem Ipsum<br>dolor<b>ab 40,50 EUR</b></div>
  <div class="prod" style="left:259px"><div class="pic" role="img" aria-label="Lederrucksack braun" style="background:linear-gradient(#7a4a2e,#3e2418)"></div>Lorem Ipsum<br>dolor<b>ab 29,50 EUR</b></div>
  <div class="prod" style="left:384px"><div class="pic" role="img" aria-label="Rucksack grau-schwarz" style="background:linear-gradient(#888,#333)"></div>Lorem Ipsum<br>dolor<b>ab 17,50 EUR</b></div>
</section>

<div class="abs rule" style="left:175px;top:538px;width:521px"></div>
<div class="abs bandhead" style="left:175px;top:549px;width:521px;border:1px solid #e6e6e6"></div>

<div class="abs col" style="left:175px;width:141px">
  <div role="img" aria-label="Frau mit Rucksack" style="height:66px;background:linear-gradient(135deg,#5a3a2a,#222 60%,#f3c9d0)"></div>
  <div style="color:var(--red);font-size:8.5px;padding:5px 20px">SUPER GÜSTIG!</div>
  <div class="para" style="padding:2px 20px;font-size:7px">Lorem ipsum dolor sit amet, consetetur sadipscing elitr, sed diam nonumy eirmod tempor...</div>
  <div style="padding:9px 20px;font-size:7px">&gt;&gt; Jetzt finden</div>
</div>
<div class="abs col" style="left:365px;width:141px"><h4>Vorteile</h4>
  <div style="margin-top:6px"></div>
  <div class="adv"><svg width="18" height="16"><path d="M2 9l5 5 9-12" stroke="#d6112a" stroke-width="3" fill="none"/></svg>Qualität vom Hersteller<small>Ab 10 Stück!</small></div>
  <div class="adv" style="margin-top:14px"><svg width="18" height="16"><path d="M2 9l5 5 9-12" stroke="#d6112a" stroke-width="3" fill="none"/></svg>Kauf auf Rechung<small>Auch ab Kleinstmengen</small></div>
  <div class="adv" style="margin-top:12px"><svg width="18" height="16"><path d="M2 9l5 5 9-12" stroke="#d6112a" stroke-width="3" fill="none"/></svg>Großes Produktportfolio für jede Art der perfekten Präsentation</div>
  <div class="adv" style="margin-top:12px"><svg width="18" height="16"><path d="M2 9l5 5 9-12" stroke="#d6112a" stroke-width="3" fill="none"/></svg>Einfach unschlagbar günstige Konditionen</div>
</div>
<div class="abs col" style="left:555px;width:141px"><h4>Unsere Angebote</h4>
  <div role="img" aria-label="Euro-Scheine und Münzen" style="position:absolute;left:0;top:62px;width:139px;height:102px;background:linear-gradient(135deg,#e7b7a8,#c9a77a 50%,#d9c6b0)"></div>
</div>
<div class="abs" style="left:551px;top:616px;width:123px;height:19px;background:linear-gradient(#e33347,var(--red-dark));color:#fff;font-size:8.5px;text-align:center;line-height:19px">Zu den Schnäppchen</div>

<div class="abs rule" style="left:175px;top:754px;width:521px"></div>
<div class="abs h2">VORMA IST IHR ANSPRECHPARTNER FÜR PRODUKTE MIT TOP PREIS/LEISTUNG VERHÄLTNIS</div>
<div class="abs tab" style="left:175px">Lorem Ipsum<br>dolor</div>
<div class="abs tab" style="left:266px">Lorem Ipsum<br>dolor</div>
<div class="abs tab" style="left:358px">Lorem Ipsum<br>dolor</div>
<div class="abs tab" style="left:453px">Lorem Ipsum<br>dolor</div>
<div class="abs tab" style="left:546px">Lorem Ipsum<br>dolor</div>
<div class="abs tab" style="left:634px">Lorem Ipsum<br>dolor</div>
<p class="abs para" style="left:175px;top:809px;width:521px">Lorem ipsum dolor sit amet, consetetur sadipscing elitr, sed diam nonumy eirmod tempor invidunt ut labore et dolore magna aliquyam erat, sed diam voluptua. At vero eos et accusam et justo duo dolores et ea rebum. Stet clita kasd gubergren, no sea takimata sanctus est Lorem ipsum dolor sit amet. Lorem ipsum dolor sit amet, consetetur sadipscing elitr, sed diam nonumy eirmod tempor invidunt ut labore et dolore magna aliquyam erat, sed diam voluptua.</p>

<div class="abs rule" style="left:32px;top:864px;width:664px"></div>
<div class="abs" style="left:32px;top:874px;width:664px;height:69px;border:1px solid #e2e2e2">
  <div class="bandhead" style="height:21px"></div>
  <p class="para" style="padding:7px 7px">Lorem ipsum dolor sit amet, consetetur sadipscing elitr, sed diam nonumy eirmod tempor invidunt ut labore et dolore magna aliquyam erat, sed diam voluptua. At vero eos et accusam et justo duo dolores et ea rebum. Stet clita kasd gubergren, no sea takimata sanctus est Lorem ipsum dolor sit amet. Lorem ipsum dolor sit amet, consetetur sadipscing elitr, sed diam nonumy eirmod tempor invidunt ut labore et dolore magna aliquyam erat, sed diam voluptua.</p>
</div>
<div class="abs rule" style="left:32px;top:952px;width:664px"></div>

<footer>
  <div class="foot-h" style="left:35px;top:964px">HILFE</div>
  <ul class="foot-list" style="left:35px;top:983px"><li>Kontakt</li><li>Geschäftskundenkontakt</li><li>Häufige Fragen &amp; Antworten</li><li>Über uns</li><li>Presse</li><li>Affliate</li></ul>
  <div class="foot-h" style="left:162px;top:964px">SERVICE</div>
  <ul class="foot-list" style="left:162px;top:983px"><li>Mein Konto</li><li>Druckvorlagen</li><li>Blog</li><li>Besonderes</li></ul>
  <div class="foot-h" style="left:288px;top:964px">INFORMATIONEN</div>
  <ul class="foot-list" style="left:288px;top:983px"><li>AGB</li><li>Versandkosten</li><li>Zahlungsmöglichkeiten</li><li>Widerrufsrecht</li><li>Datenschutzerklärung</li><li>Impressum</li></ul>

  <div class="foot-h" style="left:436px;top:964px">ZAHLUNGSMETHODEN</div>
  <div class="chips" style="left:436px;top:979px"><span class="chip">Karta</span><span class="chip">Mondokarte</span><span class="chip">Zahlfix</span></div>
  <div class="foot-h" style="left:436px;top:998px">WIR VERSCHICKEN MIT</div>
  <div class="chips" style="left:436px;top:1012px"><span class="chip" style="height:16px;line-height:15px">Paketro</span></div>
  <div class="foot-h" style="left:436px;top:1032px">SIE FINDEN UNS AUCH BEI</div>
  <div class="chips" style="left:436px;top:1046px"><span class="chip">Freundo</span><span class="chip">Kreisnet</span><span class="chip">Zwitscha</span></div>

  <div class="abs" style="left:35px;top:1080px;font-size:7.5px;color:var(--mute)">© 2013 VORMA</div>
  <div class="abs" style="left:162px;top:1080px;font-size:7.5px;color:var(--mute);line-height:11.5px">MAX Mustermann GmbH<br>Musterstraße 203<br>D- 00000 Musterstadt</div>
  <div class="abs" style="left:326px;top:1078px;font-size:6.5px;color:var(--mute);font-weight:700">RUFEN SIE UNS AN
    <svg width="14" height="12" style="vertical-align:-2px;margin-left:3px"><path d="M1 4c4-4 8-4 12 0l-2 2-2-1v-1H5v1L3 6z M3 7h8l1 4H2z" fill="#d6112a"/></svg></div>
  <div class="abs" style="left:288px;top:1092px;font-size:17px;font-weight:700;color:var(--red)">0800 00000000</div>
  <div class="abs" style="left:288px;top:1111px;font-size:7.5px;color:var(--mute);letter-spacing:.4px">MO - FR 9:00 Uhr - 18:00 Uhr</div>
  <div class="foot-h" style="left:436px;top:1080px">GEPRÜFTE SICHERHEIT</div>
  <div class="abs" style="left:436px;top:1096px;width:28px;height:28px;border-radius:50%;background:#9a9a9a" role="img" aria-label="Gütesiegel"></div>
  <div class="abs" style="left:470px;top:1094px;font-size:8px;color:var(--mute);line-height:9.8px;letter-spacing:.3px">
    ✓ &nbsp;Schnelle Lieferzeiten<br>✓ &nbsp;Käuferschutz<br>✓ &nbsp;Datenschutz<br>✓ &nbsp;21 Tage Widerrufsrecht<br>✓ &nbsp;Sichere Zahlung mit<br>✓ &nbsp;SSL - Verschlüsselung</div>
</footer>
</body>
</html>
```